Business Cards Design for the electrical wholesaler: clean bold dynamic :)

We need a business card design that would follow our latest brand guidelines. As an electrical wholesaler we want to bring a fresh look and feel into the industry. The design should be clean bold and dynamic. It should come alive with the renewed energy of our green colour. Our grey colour should keep things balanced and complement the notion of maturity and responsibility. We employ Lato as a corporate font however are not bound by this font and we’re open to interpretation here.

Target Market(s)

Electrical contractors

Industry/Entity Type

Business

Contact Information for Business Card

Logo
Name & Surname: Olena Dovbush
Job Title: Director of Marketing
Email: helen.dovbush@mailvane.example
Cell phone: XXX.XXX.XXXX
Address: 20917 - 87 Ave. Edmonton, AB, Canada. T6K 2R8
Business Phone: 780.555.0187
Website: www.qorvil.example

Font styles to use
Other font styles liked:
• Lato

Requirements
Must have
• Logo & website
Nice to have
• Brand elements - some of them you may find in the attached Brand Guidelines (e.g. three lines on the background signifying "W")

```html
<!DOCTYPE html>
<html lang="en">
<head>
<meta charset="utf-8">
<title>Qorvil Business Cards</title>
<link href="https://fonts.googleapis.com/css2?family=Lato:wght@400;700;900&display=swap" rel="stylesheet">
<style>
  :root {
    --brand-green: #8dc342;
    --brand-grey: #4d4d4f;
    --ribbon-fold: #2f2f31;
    --ink: #222222;
    --paper: #ffffff;
    --backdrop: #d3e6ec;
    --shadow: rgba(40, 60, 70, 0.22);
  }
  * { box-sizing: border-box; margin: 0; padding: 0; }
  html, body { width: 1200px; height: 900px; overflow: hidden; }
  body {
    background: var(--backdrop);
    font-family: "Lato", sans-serif;
    position: relative;
  }
  .card {
    position: absolute;
    width: 600px;
    height: 343px;
    box-shadow: 0 10px 24px var(--shadow);
    overflow: hidden;
  }

  /* Front */
  .card-front {
    left: 60px; top: 60px;
    background: var(--brand-green);
  }
  .front-brand {
    position: absolute;
    left: 0; right: 0; top: 120px;
    display: flex; justify-content: center; align-items: center; gap: 18px;
  }
  .front-brand .brand-mark {
    width: 54px; height: 54px; border-radius: 50%;
    background: var(--brand-grey);
  }
  .front-brand .brand-name {
    font-size: 76px; font-weight: 700; color: var(--brand-grey);
    line-height: 1; letter-spacing: -1px;
  }
  .front-web {
    position: absolute; left: 0; right: 0; bottom: 34px;
    text-align: center; font-size: 14px; color: #2e2e30;
  }

  /* Back */
  .card-back {
    left: 540px; top: 497px;
    background: var(--paper);
  }
  .back-panel { position: absolute; inset: 0; }
  .back-brand {
    position: absolute; left: 34px; top: 78px;
    display: flex; align-items: center; gap: 12px;
  }
  .back-brand .brand-mark {
    width: 30px; height: 30px; background: var(--brand-green);
  }
  .back-brand .brand-name {
    font-size: 48px; font-weight: 700; color: var(--brand-grey);
    line-height: 1; letter-spacing: -0.5px;
  }
  .name-ribbon {
    position: absolute; left: 308px; top: 42px;
    width: 292px; height: 64px;
    background: var(--brand-grey);
    color: #fff;
    padding: 12px 0 0 46px;
  }
  .name-ribbon .person-name { font-size: 20px; font-weight: 700; }
  .name-ribbon .person-title { font-size: 12px; margin-top: 3px; }
  .ribbon-fold { position: absolute; left: 308px; top: 106px; }

  .contact-list {
    position: absolute; left: 30px; bottom: 24px;
    list-style: none;
  }
  .contact-list li {
    display: flex; align-items: center; gap: 10px;
    font-size: 13px; color: var(--ink); height: 26px;
  }
  .contact-icon {
    width: 20px; height: 20px; background: var(--brand-green);
    display: flex; align-items: center; justify-content: center;
    flex: none;
  }
  .address-block {
    position: absolute; right: 30px; bottom: 58px; width: 240px;
    text-align: center; color: #fff; font-size: 14px; line-height: 1.45;
  }
  .address-block svg { display: block; margin: 0 auto 8px; }
</style>
</head>
<body>

<section class="card card-front" aria-label="Business card front">
  <div class="front-brand">
    <span class="brand-mark"></span>
    <span class="brand-name">Qorvil</span>
  </div>
  <p class="front-web">www.qorvil.example</p>
</section>

<section class="card card-back" aria-label="Business card back">
  <svg class="back-panel" width="600" height="343" viewBox="0 0 600 343">
    <polygon points="340,0 600,0 600,343 272,343" fill="var(--brand-green)"/>
  </svg>

  <div class="back-brand">
    <span class="brand-mark"></span>
    <span class="brand-name">Qorvil</span>
  </div>

  <div class="name-ribbon">
    <p class="person-name">Olena Dovbush</p>
    <p class="person-title">Director of Marketing</p>
  </div>
  <svg class="ribbon-fold" width="24" height="18" viewBox="0 0 24 18">
    <polygon points="0,0 22,0 22,18" fill="var(--ribbon-fold)"/>
  </svg>

  <ul class="contact-list">
    <li><span class="contact-icon">
      <svg width="12" height="12" viewBox="0 0 24 24"><path d="M6.6 10.8a15 15 0 0 0 6.6 6.6l2.2-2.2a1 1 0 0 1 1-.25 11.4 11.4 0 0 0 3.6.57 1 1 0 0 1 1 1V20a1 1 0 0 1-1 1A17 17 0 0 1 3 4a1 1 0 0 1 1-1h3.5a1 1 0 0 1 1 1c0 1.25.2 2.45.57 3.57a1 1 0 0 1-.25 1z" fill="#fff"/></svg>
    </span>780-555-0142</li>
    <li><span class="contact-icon">
      <svg width="12" height="12" viewBox="0 0 24 24"><rect x="3" y="8" width="18" height="12" rx="2" fill="none" stroke="#fff" stroke-width="2"/><path d="M6 8V5h12v3" fill="none" stroke="#fff" stroke-width="2"/><circle cx="12" cy="14" r="2.5" fill="#fff"/></svg>
    </span>780-555-0187</li>
    <li><span class="contact-icon">
      <svg width="12" height="12" viewBox="0 0 24 24"><rect x="2" y="5" width="20" height="14" fill="none" stroke="#fff" stroke-width="2"/><path d="M2 5l10 8 10-8" fill="none" stroke="#fff" stroke-width="2"/></svg>
    </span>helen.dovbush@mailvane.example</li>
    <li><span class="contact-icon">
      <svg width="12" height="12" viewBox="0 0 24 24"><circle cx="12" cy="12" r="9" fill="none" stroke="#fff" stroke-width="2"/><path d="M3 12h18M12 3c3 3 3 15 0 18M12 3c-3 3-3 15 0 18" fill="none" stroke="#fff" stroke-width="1.6"/></svg>
    </span>www.qorvil.example</li>
  </ul>

  <div class="address-block">
    <svg width="14" height="18" viewBox="0 0 24 30"><path d="M12 0a10 10 0 0 0-10 10c0 7.5 10 20 10 20s10-12.5 10-20A10 10 0 0 0 12 0z" fill="#fff"/><circle cx="12" cy="10" r="4" fill="var(--brand-green)"/></svg>
    <p>20917 - 87 Ave. Edmonton, AB,<br>Canada. T6K 2R8</p>
  </div>
</section>

</body>
</html>
```